Redesign and move to Wordpress for quarvendo.com

Our website needs a redesign and at the same time we are moving it to Wordpress. Please help us with a new digital professional look and feel.

We are an Australian Software Engineering company specialising in advanced software development using in A.I., PLatform Engineering, Integration and Cloud. See the current quarvendo.com for more information about us.

```html
<!DOCTYPE html>
<html lang="en">
<head>
<meta charset="utf-8">
<title>Quarvendo — Software Engineering</title>
<link href="https://fonts.googleapis.com/css2?family=Michroma&family=Roboto:wght@300;400;500;700&family=Roboto+Slab:wght@700&display=swap" rel="stylesheet">
<style>
:root{
  --navy:#0a1528;
  --dark:#161618;
  --card:#2a2a2c;
  --teal:#3bb8b4;
  --blue:#1c5ea8;
  --deep-blue:#1a4f92;
  --white:#ffffff;
  --text:#555b63;
  --light:#f3f4f5;
}
*{margin:0;padding:0;box-sizing:border-box}
html,body{width:1200px;height:4890px;overflow:hidden}
body{position:relative;background:var(--white);font-family:'Roboto',sans-serif;color:var(--text)}
.abs{position:absolute}
.bands{position:absolute;left:0;top:0}
.brand{display:flex;align-items:center;gap:18px;color:var(--white);font-weight:300;font-size:40px;letter-spacing:2px}
.brand-mark{width:62px;height:62px;border:5px solid var(--teal)}
.nav{display:flex;gap:36px;font-size:15px;letter-spacing:1px;color:var(--white)}
.nav .active{color:var(--teal)}
.search{width:52px;height:52px;border:2px solid var(--teal);border-radius:50%;display:flex;align-items:center;justify-content:center}
.btn{display:inline-block;background:linear-gradient(90deg,var(--teal),var(--blue));color:var(--white);font-weight:700;font-size:15px;letter-spacing:1.5px;padding:18px 26px;border-radius:30px}
.eyebrow{font-size:15px;font-weight:700;letter-spacing:2px;color:var(--teal);display:flex;align-items:center;gap:10px}
.eyebrow::before,.eyebrow::after{content:"";width:36px;height:3px;background:var(--teal)}
.eyebrow.left::before{display:none}
.title{font-family:'Michroma',sans-serif;font-size:32px;letter-spacing:1px}
.center{left:0;width:1200px;text-align:center;display:flex;justify-content:center}
.photo{border-radius:0}
.frame{position:absolute;padding:10px}
.frame div{width:100%;height:100%}
.about-text p{font-size:15.5px;line-height:26px;margin-bottom:12px}
.service{position:absolute;width:297px;height:280px;background:var(--card);color:var(--white);text-align:center;padding:20px 22px}
.service.featured{background:linear-gradient(135deg,var(--teal),var(--blue))}
.service h3{font-size:15px;font-weight:700;letter-spacing:.5px;line-height:26px;margin-top:14px}
.service p{font-size:14.5px;line-height:24px;color:#d8d8d8;margin-top:12px;font-weight:300}
.service.featured p{color:#eef}
.service .arrow{margin-top:12px}
.blog{position:absolute;width:296px;height:405px;background:var(--white);box-shadow:0 2px 10px rgba(0,0,0,.12)}
.blog.featured{background:linear-gradient(135deg,var(--teal),var(--blue));color:var(--white)}
.blog h4{font-size:14px;font-weight:700;letter-spacing:.5px;margin:30px 14px 16px;color:#222}
.blog.featured h4{color:var(--white)}
.blog p{font-size:14px;line-height:22.5px;margin:0 14px}
.blog a{color:var(--teal);text-decoration:underline}
.blog.featured a{color:var(--white)}
.blog .corner{position:absolute;right:0;bottom:0;width:38px;height:34px;background:var(--blue);border-radius:10px 0 0 0}
.blog.featured .corner{background:var(--white)}
.slide{width:38px;height:38px;border-radius:50%;display:flex;align-items:center;justify-content:center}
.calendar{position:absolute;left:152px;top:3265px;width:370px;height:372px;background:var(--white);border-radius:20px;overflow:hidden;box-shadow:0 6px 16px rgba(0,0,0,.35)}
.cal-head{height:100px;background:linear-gradient(180deg,#5cc8c4,var(--teal));color:var(--white);text-align:center;padding-top:18px}
.cal-head strong{display:block;font-size:32px;letter-spacing:2px}
.cal-head span{font-size:24px}
.calendar table{width:100%;border-collapse:collapse;font-weight:700;font-size:14px;color:#222;text-align:center;margin-top:10px}
.calendar td,.calendar th{height:36px}
.calendar .sun{color:#d9262b}
.calendar .today span{background:var(--blue);color:var(--white);padding:5px 5px}
.partner{position:absolute;top:3962px;width:228px;height:162px;background:var(--light);display:flex;align-items:center;justify-content:center}
.partner.featured{background:var(--deep-blue);border:6px solid var(--blue)}
.news h2{font-family:'Roboto Slab',serif;color:var(--white);font-size:20px;line-height:26px}
.news small{display:block;color:var(--white);font-size:11px;font-weight:700;letter-spacing:.5px;margin-top:12px}
.email{position:absolute;left:680px;top:4364px;width:382px;height:54px;background:var(--white);border-radius:30px;font-size:12px;color:#888;padding:20px 22px}
.send{position:absolute;right:4px;top:4px;width:46px;height:46px;border-radius:50%;background:var(--blue);border:3px solid var(--white);box-shadow:0 0 0 2px var(--blue)}
.footer h5{font-size:17px;font-weight:700;color:var(--white);letter-spacing:.5px}
.footer p,.footer li{color:var(--white);font-size:14.5px}
.links li{list-style:none;margin-top:22px}
.contact-item{display:flex;gap:14px;margin-top:24px}
.contact-item .ic{width:40px;height:40px;border-radius:50%;background:var(--blue);flex:none;display:flex;align-items:center;justify-content:center}
.contact-item b{display:block;font-size:14px}
.social{display:flex;gap:14px;margin-top:28px}
.social span{width:38px;height:38px;border-radius:50%;border:2px solid var(--white);display:flex;align-items:center;justify-content:center;font-size:11px;color:var(--white)}
.social span.fb{background:var(--blue);border-color:var(--blue)}
</style>
</head>
<body>

<svg class="bands" width="1200" height="4890" viewBox="0 0 1200 4890" aria-hidden="true">
  <defs>
    <linearGradient id="heroGrad" x1="0" y1="0" x2="0" y2="1">
      <stop offset="0" stop-color="#0c1b33"/><stop offset="1" stop-color="#081122"/>
    </linearGradient>
    <linearGradient id="blueGrad" x1="0" y1="0" x2="1" y2="0">
      <stop offset="0" stop-color="#3bb8b4"/><stop offset="1" stop-color="#1c5ea8"/>
    </linearGradient>
  </defs>
  <polygon points="0,0 1200,0 1200,520 0,612" fill="url(#heroGrad)"/>
  <polygon points="440,612 1200,505 1200,590" fill="url(#blueGrad)"/>
  <polygon points="0,1212 720,1255 0,1310" fill="#3bb8b4"/>
  <polygon points="0,1310 1200,1210 1200,2280 0,2280" fill="#111214"/>
  <polygon points="660,2280 1200,2180 1200,2310" fill="url(#blueGrad)"/>
  <polygon points="0,2935 820,2992 0,3035" fill="#3bb8b4"/>
  <polygon points="0,3035 1200,2975 1200,3725 0,3790" fill="#1c1c1f"/>
  <polygon points="520,3790 1200,3700 1200,3812" fill="url(#blueGrad)"/>
  <polygon points="0,4180 700,4255 0,4310" fill="#3bb8b4"/>
  <polygon points="0,4310 1200,4245 1200,4512 0,4512" fill="#1c5ea8"/>
  <rect x="0" y="4512" width="1200" height="378" fill="#111214"/>
</svg>

<!-- Header -->
<header>
  <div class="abs brand" style="left:104px;top:26px"><span class="brand-mark"></span>quarvendo</div>
  <nav class="abs nav" style="left:562px;top:48px">
    <span class="active">HOME</span><span>ABOUT</span><span>SERVICES</span><span>BLOG</span><span>CONTACT</span>
  </nav>
  <div class="abs search" style="left:1043px;top:30px">
    <svg width="20" height="20" viewBox="0 0 20 20"><circle cx="8" cy="8" r="6" fill="none" stroke="#fff" stroke-width="2.5"/><line x1="12.5" y1="12.5" x2="18" y2="18" stroke="#fff" stroke-width="2.5"/></svg>
  </div>
</header>

<!-- Hero -->
<section class="hero">
  <div class="abs" role="img" aria-label="Hand reaching toward a glowing AI circuit chip" style="left:620px;top:0;width:580px;height:540px;background:radial-gradient(circle at 55% 40%,#3f7fd0 0%,#1d3f80 30%,rgba(12,27,51,0) 70%)"></div>
  <p class="abs" style="left:104px;top:214px;color:#fff;font-size:27px;letter-spacing:3px">WELCOME TO</p>
  <div class="abs" style="left:50px;top:276px;display:flex;flex-direction:column;gap:10px">
    <span style="width:8px;height:8px;border-radius:50%;background:#fff"></span><span style="width:8px;height:8px;border-radius:50%;background:#fff"></span><span style="width:8px;height:8px;border-radius:50%;background:#fff"></span>
  </div>
  <h1 class="abs" style="left:100px;top:262px;font-family:'Michroma',sans-serif;font-size:58px;color:var(--teal);letter-spacing:2px;font-weight:400">QUARVENDO</h1>
  <span class="abs btn" style="left:104px;top:354px">GET STARTED</span>
</section>

<!-- About -->
<section class="about">
  <div class="frame" style="left:104px;top:695px;width:234px;height:165px;background:var(--blue)"><div role="img" aria-label="Glowing AI chip graphic" style="background:radial-gradient(circle,#3a7de0,#0b1f6a)"></div></div>
  <div class="frame" style="left:348px;top:695px;width:234px;height:258px;background:var(--blue)"><div role="img" aria-label="Robotic hand touching a human hand" style="background:linear-gradient(135deg,#2b4a6a,#0c1724)"></div></div>
  <div class="frame" style="left:104px;top:870px;width:234px;height:258px;background:var(--teal)"><div role="img" aria-label="Engineer working at multiple monitors" style="background:linear-gradient(135deg,#3d4f66,#121a26)"></div></div>
  <div class="frame" style="left:348px;top:963px;width:234px;height:165px;background:var(--teal)"><div role="img" aria-label="Team working in an operations room" style="background:linear-gradient(135deg,#3a5a7a,#0f1a28)"></div></div>

  <div class="abs eyebrow left" style="left:640px;top:703px;display:flex;flex-direction:row-reverse;justify-content:flex-end">ABOUT US</div>
  <h2 class="abs title" style="left:640px;top:730px;color:var(--blue)">WHO WE ARE</h2>
  <div class="abs about-text" style="left:640px;top:793px;width:460px">
    <p>Since our inception in 2013, we have been on a mission to make complex custom enterprise integration accessible to any organization, regardless of industry, size, or location.</p>
    <p>At Quarvendo, we craft bespoke software solutions that are not available on the market. By building organizations market-leading products, process automation, legacy system enablement, or advanced intelligent systems, we empower our customers to achieve a competitive edge in their industry.</p>
  </div>
  <span class="abs btn" style="left:640px;top:1032px">READ MORE</span>
</section>

<!-- Services -->
<section class="services">
  <div class="abs center eyebrow" style="top:1344px">OUR SERVICES</div>
  <h2 class="abs center title" style="top:1374px;color:#fff">WHAT WE DO</h2>

  <article class="service" style="left:106px;top:1467px">
    <svg width="60" height="60" viewBox="0 0 60 60"><circle cx="30" cy="30" r="18" fill="none" stroke="#fff" stroke-width="2"/><circle cx="30" cy="30" r="7" fill="none" stroke="#fff" stroke-width="2"/></svg>
    <h3>ENTERPRISE SYSTEMS<br>INTEGRATION</h3>
    <p>Automate your business processes internally or externally to improve data quality and process</p>
    <div class="arrow">→</div>
  </article>
  <article class="service featured" style="left:454px;top:1467px">
    <svg width="60" height="60" viewBox="0 0 60 60"><circle cx="30" cy="30" r="18" fill="none" stroke="#fff" stroke-width="2"/><rect x="22" y="22" width="16" height="16" fill="none" stroke="#fff" stroke-width="2"/></svg>
    <h3>MICRO<br>SERVICES</h3>
    <p>Leverage Microservices Architecture to enable quick deployment, dynamically scalable service performance.</p>
    <div class="arrow">→</div>
  </article>
  <article class="service" style="left:800px;top:1467px">
    <svg width="60" height="60" viewBox="0 0 60 60"><circle cx="30" cy="30" r="20" fill="none" stroke="#fff" stroke-width="2"/><circle cx="30" cy="30" r="9" fill="none" stroke="#fff" stroke-width="2"/></svg>
    <h3>PLATFORM<br>ENGINEERING</h3>
    <p>For organisations looking to manage the security and cost risks around their cloud infrastructure for</p>
    <div class="arrow">→</div>
  </article>
  <article class="service" style="left:106px;top:1795px">
    <svg width="60" height="60" viewBox="0 0 60 60"><rect x="14" y="14" width="32" height="32" fill="none" stroke="#fff" stroke-width="2"/><rect x="22" y="22" width="16" height="16" fill="none" stroke="#fff" stroke-width="2"/></svg>
    <h3>CONVERSATIONAL<br>AI</h3>
    <p>Enabling legacy systems with conversational user interfaces, or simply building intelligent</p>
    <div class="arrow">→</div>
  </article>
  <article class="service" style="left:454px;top:1795px">
    <svg width="60" height="60" viewBox="0 0 60 60"><circle cx="30" cy="30" r="20" fill="none" stroke="#fff" stroke-width="2"/><rect x="24" y="20" width="12" height="20" fill="none" stroke="#fff" stroke-width="2"/></svg>
    <h3>COPILOT / AI<br>AGENTS</h3>
    <p>The future of business AI are autonomous agents that specialise in your business data and processes.</p>
    <div class="arrow">→</div>
  </article>
  <article class="service" style="left:800px;top:1795px">
    <svg width="60" height="60" viewBox="0 0 60 60"><path d="M12 18h36M30 18v24M18 42h24" fill="none" stroke="#fff" stroke-width="2"/><circle cx="30" cy="30" r="5" fill="none" stroke="#fff" stroke-width="2"/></svg>
    <h3>REAL-TIME DATA STREAM<br>PROCESSING</h3>
    <p>Being able to react to changing business conditions in a precise intelligent way is becoming</p>
    <div class="arrow">→</div>
  </article>
  <span class="abs btn" style="left:524px;top:2103px">VIEW MORE</span>
</section>

<!-- Blog -->
<section class="news-articles">
  <div class="abs center eyebrow" style="top:2330px">OUR BLOGS</div>
  <h2 class="abs center title" style="top:2360px;color:var(--blue)">NEWS &amp; ARTICLES</h2>

  <div class="abs slide" style="left:40px;top:2630px;border:2px solid #333"><svg width="10" height="12" viewBox="0 0 10 12"><path d="M7 1L2 6l5 5" fill="none" stroke="#333" stroke-width="2"/></svg></div>
  <div class="abs slide" style="left:1120px;top:2630px;background:var(--blue)"><svg width="10" height="12" viewBox="0 0 10 12"><path d="M3 1l5 5-5 5" fill="none" stroke="#fff" stroke-width="2"/></svg></div>

  <article class="blog" style="left:104px;top:2445px">
    <div role="img" aria-label="Laptop with floating AI interface graphics" style="height:168px;background:linear-gradient(135deg,#9fb4c6,#3c4f63)"></div>
    <h4>AI IN SOFTWARE ENGINEERING</h4>
    <p><a>10 unexpected ways to use CodeMate Pilot</a> (DevHub Blog) CodeMate Pilot is widely known for its code generation feature. Learn how the AI assistant's abilities can extend beyond just code generation.</p>
    <span class="corner"></span>
  </article>
  <article class="blog featured" style="left:441px;top:2445px;width:316px">
    <div role="img" aria-label="Two colleagues reviewing code on a laptop" style="height:168px;background:linear-gradient(135deg,#7b6a5a,#2c2a2a)"></div>
    <h4>INDUSTRY RESEARCH</h4>
    <p><a>PROMTA: A general-purpose framework for prompt optimization</a> (Northwind Research) Large language models (LLMs) have revolutionized various tasks, but prompt engineering remains a challenge. Enter PROMTA: an open-source</p>
    <span class="corner"></span>
  </article>
  <article class="blog" style="left:801px;top:2445px">
    <div role="img" aria-label="Robot hands typing on a laptop with data graphics" style="height:168px;background:linear-gradient(135deg,#2f8a9a,#0c2430)"></div>
    <h4>BUSINESS INSIGHTS</h4>
    <p><a>How Storytelling Helps Data-driven Teams Succeed</a> (Harbor School of Management) Winning leaders know that data alone isn't enough. It's the art of storytelling that drives sustained performance. In the spring of 2014,</p>
    <span class="corner"></span>
  </article>
</section>

<!-- Booking -->
<section class="booking">
  <div class="abs" role="img" aria-label="Portrait of the lead technologist" style="left:600px;top:3200px;width:600px;height:560px;background:radial-gradient(ellipse at 60% 40%,#7a6f68 0%,#3a3636 45%,rgba(28,28,31,0) 75%)"></div>
  <div class="abs center eyebrow" style="top:3067px">BOOKING</div>
  <h2 class="abs center title" style="top:3108px;color:#fff;font-size:32px;line-height:42px;text-align:center">BOOK AN OBLIGATION FREE CONSULTATION<br>WITH OUR LEAD TECHNOLOGIST</h2>

  <div class="calendar">
    <div class="cal-head"><strong>JANUARY</strong><span>2025</span></div>
    <table>
      <tr><th>Mon</th><th>Tue</th><th>Wed</th><th>Thu</th><th>Fri</th><th>Sat</th><th class="sun">Sun</th></tr>
      <tr><td></td><td></td><td></td><td></td><td></td><td></td><td class="sun">1</td></tr>
      <tr><td>2</td><td>3</td><td>4</td><td>5</td><td>6</td><td>7</td><td>8</td></tr>
      <tr><td>9</td><td>10</td><td>11</td><td>12</td><td>13</td><td>14</td><td>15</td></tr>
      <tr><td>16</td><td>17</td><td>18</td><td>19</td><td>20</td><td>21</td><td class="today"><span>22</span></td></tr>
      <tr><td>23</td><td>24</td><td>25</td><td>26</td><td>27</td><td>28</td><td>29</td></tr>
      <tr><td>30</td><td>31</td><td></td><td></td><td></td><td></td><td></td></tr>
    </table>
  </div>
  <svg class="abs" style="left:520px;top:3540px" width="50" height="130" viewBox="0 0 50 130"><path d="M4 6 C45 20 48 80 34 120" fill="none" stroke="#fff" stroke-width="2"/><path d="M26 110 L34 122 L42 110" fill="none" stroke="#fff" stroke-width="2"/></svg>
  <span class="abs btn" style="left:156px;top:3665px">LEARN MORE</span>
  <p class="abs" style="left:323px;top:3676px;color:#fff;font-size:24px;font-weight:700;font-style:italic">Meet With Our CTO</p>
</section>

<!-- Partners -->
<section class="partners">
  <div class="abs center eyebrow" style="top:3850px">OUR MUMBERS</div>
  <h2 class="abs center title" style="top:3880px;color:var(--blue)">OUR PARTNERS</h2>
  <div class="partner" style="left:104px" role="img" aria-label="Partner badge: Veldra"><span style="width:110px;height:44px;background:#222"></span></div>
  <div class="partner featured" style="left:361px" role="img" aria-label="Partner badge: Corvanta"><span style="width:62px;height:62px;background:#fff"></span></div>
  <div class="partner" style="left:614px" role="img" aria-label="Partner badge: Trellway"><span style="width:150px;height:60px;border:4px solid #222;border-radius:8px"></span></div>
  <div class="partner" style="left:868px" role="img" aria-label="Partner badge: Brightfund"><span style="width:120px;height:30px;background:#333;border-radius:15px"></span></div>
</section>

<!-- Newsletter -->
<section class="news">
  <div class="abs" style="left:130px;top:4368px;width:520px">
    <h2>LOREM IPSUM DOLOR SIT AMET, CONSECT ETUR ADIPISCING ELIT, SED DO.</h2>
    <small>REGISTER TO OUR NEWSLETTER TO FIND OUT MORE.</small>
  </div>
  <div class="email">Email Address
    <span class="send"><svg width="40" height="40" viewBox="0 0 40 40"><path d="M10 20 L30 11 L24 30 L20 22 Z" fill="none" stroke="#fff" stroke-width="2"/></svg></span>
  </div>
</section>

<!-- Footer -->
<footer class="footer">
  <div class="abs brand" style="left:104px;top:4592px"><span class="brand-mark"></span>quarvendo</div>
  <p class="abs" style="left:104px;top:4678px;width:330px;font-size:12.5px;line-height:22px">Lorem ipsum dolor sit amet, consectetur adipiscing elit, sed do eiusmod tempor incididunt ut labore et dolore magna aliqua. Quis ipsum suspendisse ultrices gravida. Risus commodo viverra maecenas accumsan lacus vel facilisis.</p>

  <div class="abs" style="left:505px;top:4584px">
    <h5>QUICK LINKS</h5>
    <ul class="links"><li><b>Home</b></li><li>About</li><li>Services</li><li>Blog</li><li>Contact</li></ul>
  </div>

  <div class="abs" style="left:683px;top:4582px">
    <h5>CONTACT US</h5>
    <div class="contact-item"><span class="ic"><svg width="18" height="18" viewBox="0 0 18 18"><path d="M4 2l3 3-2 2c1 2 3 4 5 5l2-2 3 3-2 3C7 16 2 11 1 4z" fill="#fff"/></svg></span><p><b>PHONE NO:</b>1800 562 907</p></div>
    <div class="contact-item"><span class="ic"><svg width="18" height="14" viewBox="0 0 18 14"><rect x="1" y="1" width="16" height="12" fill="none" stroke="#fff" stroke-width="2"/><path d="M1 1l8 6 8-6" fill="none" stroke="#fff" stroke-width="2"/></svg></span><p><b>EMAIL:</b>info@quarvendo.com</p></div>
    <div class="contact-item"><span class="ic"><svg width="14" height="18" viewBox="0 0 14 18"><path d="M7 17C3 11 1 8 1 6a6 6 0 0112 0c0 2-2 5-6 11z" fill="#fff"/><circle cx="7" cy="6" r="2" fill="#1c5ea8"/></svg></span><p><b>LOCATION:</b>Suite 402, 28 Harbourview Lane<br>Melbourne, VIC , 3006</p></div>
  </div>

  <div class="abs" style="left:960px;top:4582px">
    <h5>SOCIAL MEDIAS</h5>
    <div class="social"><span class="fb" aria-label="Social profile"></span><span aria-label="Social profile"></span><span aria-label="Social profile"></span></div>
  </div>

  <p class="abs" style="left:0;width:1200px;top:4852px;text-align:center;font-size:12px;color:#fff">Copyright © 2025 Quarvendo | All Rights Reserved</p>
</footer>

</body>
</html>
```